Website design for Australia Equine Insurance business

Website Design Brief
1. Introduction
This brief guides the development of a modern, interactive website for our next-generation equine insurance business. We aim to establish a strong digital presence with a website that embodies innovation, usability, and trust, leading to exceptional user experiences and high customer conversions.

2. Company Background
Our startup offers cutting-edge equine insurance solutions across Australia, leveraging emerging technologies for smarter risk assessment, customer engagement, and claims processing. Our commitment is to protect our customers' financial interests and their equine companions with unparalleled service and modern, flexible insurance options.

3. Objectives
The website should:

Highlight our innovative products, services, and unique value proposition.
Drive lead generation and customer conversion using engaging design elements and compelling CTAs.
Foster customer trust and loyalty through transparency, industry expertise, and interactive features.
Enable users to request quotes, purchase insurance, and file claims online in a seamless, intuitive manner.
Be responsive and user-friendly across all devices.

5. Design Requirements
Look and Feel
The design should reflect our brand's personality: innovative, modern, reliable, and committed to the equine community. It should use our brand colours and logo, ensuring a clean, fresh aesthetic. The style guide should promote consistency across fonts, buttons, form fields, etc.

User Interface
The website should display optimally across desktop, tablet, and mobile, with a focus on usability and accessibility. Clear navigation menus, intuitive search and filters, and easy access to important pages like "Get a Quote," "File a Claim," "Contact Us," etc., should be ensured.

Content
Content should be engaging, easily digestible, and serve to educate users about our unique services and the value of equine insurance. The site should also feature blog posts, video guides, and interactive FAQs to illustrate our industry expertise and the benefits of our next-gen approach.

Functionality
Smart Quote Calculator: An AI-driven quote calculator providing real-time estimates.
Digital Purchase and Claims: Facilitate insurance purchase and claims filing digitally, complemented by AI and blockchain tech for efficiency and transparency.
User Accounts: Customers should be able to manage their policies, payments, and claims through personalized accounts.
AI Chatbot: Implement a chatbot for automated customer support, query resolution, and guidance.
SEO and Analytics: Ensure the website is SEO-optimized and integrated with analytics tools like Google Analytics.
6. Timeline
We aim to complete the website design and development project within a 4-month timeframe, given the startup nature of our business. This includes stages of initial design, content creation, development, testing, and launch.

7. Budget
We understand the importance of investing in quality and are open to reasonable negotiations for ensuring the best output.

Target Market(s)

4. Target Audience Our target audience is tech-savvy horse owners, breeders, trainers, equestrian centres, and younger individuals interested in equine ownership, primarily aged between 18-45. They appreciate digital convenience, technological innovation, and quality service.

Industry/Entity Type

The equine insurance industry is a specialised branch of the broader insurance market, focusing on coverage for all things related to horses. It encompasses a wide range of coverage areas such as mortality insurance (life insurance for horses), medical coverage, loss of use, liability coverage, and more. The industry is one of passion and care, where the clientele often form a deeply emotional connection to their insured assets - their horses. It’s characterized by a strong focus on well-being, safety, and the financial protection of both the horses and their owners. This makes trust, professionalism, and expertise central to any successful equine insurance business. Our new venture is positioned as a next-generation equine insurance provider. This means we are blending traditional insurance offerings with cutting-edge technologies such as AI and machine learning for better risk assessment, seamless customer service, and efficient claims processing. The audience in this sector is diverse, ranging from individual horse owners and breeders to professional trainers and large equestrian centres. Many of our customers have a significant emotional and financial investment in their horses, so they need to feel reassured that their insurance provider understands and respects this. In designing for this industry, it's essential to strike a balance between sophistication and warmth, to reflect both our professional reliability and our understanding of the personal passion that drives our clients. The design needs to feel modern and innovative, signaling our next-gen approach, but also trustworthy and user-friendly, ensuring customers of all technological skill levels feel comfortable using our platform. Moreover, the design should convey a sense of our commitment to the equine community, showing that we're more than just a faceless corporation. We care deeply about the wellbeing of horses and their owners, and we're here to support them with quality insurance solutions tailored to their unique needs.

Coding

Coded - Design and coding required

Number of Pages Required

5+ page

Requirements
Must have
• Responsive Design: The website should be fully responsive, offering optimal viewing and interaction across a range of devices - desktop, tablet, and mobile. Intuitive Navigation: The site should feature an easy-to-understand navigation system that allows users to find the information they're seeking quickly and efficiently. Clear Branding: The design should consistently incorporate the company's logo, colors, and overall aesthetic, reinforcing brand recognition. Content: High-quality, relevant content that explains your services, highlights your unique selling propositions, and educates users about equine insurance. The language should be clear, concise, and engaging. Smart Quote Calculator: An interactive tool enabling potential customers to get real-time insurance quotes. Online Purchase and Claims Filing System: A streamlined, user-friendly process for customers to buy insurance and file claims online. Customer Accounts: A secure area for customers to manage their policies, track claims, and make payments. AI Chatbot: An automated chat feature providing immediate customer support and answering frequently asked questions. SEO Optimization: The site must be search engine friendly, with strategically placed keywords, meta tags, and an XML sitemap for better indexing by search engines. Analytics Integration: Integration with tools like Google Analytics for tracking and analyzing user behavior and site performance. Data Security: Implementation of strong security measures to protect user data, including SSL encryption. Accessibility: Compliance with Web Content Accessibility Guidelines (WCAG) to ensure the site is accessible to people with disabilities. Contact Information: Clearly visible and easily accessible contact details, including phone number, email, and physical address. Social Media Integration: Links to the company's social media profiles for enhanced customer engagement and brand visibility. Remember, while these are essential features, the goal should always be to provide a seamless, positive user experience that aligns with your brand's identity and goals.
Nice to have
• Interactive Features: Interactive elements like quizzes or calculators can engage users, offer value, and make your site more memorable. Video Content: Videos explaining your products, services, or the importance of equine insurance can be a dynamic way to share information and appeal to different learning styles. Live Chat: In addition to an AI chatbot, having a live chat option for immediate customer support could significantly enhance user experience and satisfaction. Personalisation: If your resources allow, personalised content based on user behaviour or preferences can make your website more engaging and relevant. Integrated Blog: A blog section featuring articles on equine health, insurance tips, case studies etc., could help establish your brand as a thought leader in the field and improve SEO. Multilingual Support: If your target audience includes non-English speakers, offering content in multiple languages could be a beneficial feature. Customer Testimonials/Reviews: Including testimonials or reviews from satisfied customers can build trust and offer social proof. Resource Library: A library of downloadable resources (guides, checklists, eBooks) could offer added value to your customers and potential leads. Interactive FAQ: A dynamic FAQ section, where users can find answers quickly, or even an FAQ chatbot, could enhance the user experience. Newsletter Signup: An easily accessible sign-up option for a regular newsletter to keep users informed about your services, industry news, and tips. Integration with Customer Relationship Management (CRM) Software: To manage leads and customer information effectively, if your business operations allow for this level of integration.
Should not have
• Cluttered Layout: Overcrowding pages with too much information, images, or other elements can make your website look messy and confusing, hindering usability. Irrelevant Content: Your website should focus on information that is relevant to your target audience and industry. Avoid including content that does not provide value or enhance understanding of your products or services. Complex Navigation: A website should not have a confusing navigation system. Users should be able to find what they're looking for quickly and easily. Inconsistent Design: Inconsistencies in fonts, colors, or overall design can make your website look unprofessional. The design should be consistent throughout all pages. Slow Loading Times: Large images, animations, or other elements that significantly slow down page loading times should be avoided. Slow websites can lead to a poor user experience and high bounce rates. Poor Mobile Experience: Given the prevalence of mobile browsing, a design that doesn't perform well on mobile devices is a definite no. Autoplay Media: Videos or audio clips that start playing automatically can be annoying to users and should generally be avoided. Inaccessible Content: Ensure that all content is accessible to users of all abilities. Avoid design elements that violate accessibility standards. Hidden Contact Information: Contact information should be easy to find. Do not hide it in obscure parts of the website. Pop-ups: While sometimes necessary for marketing strategies, excessive use of pop-ups can annoy users and distract from the main content. Outdated Plugins: Avoid using outdated plugins or technology that some users may not be able to load or that could pose security risks. Lack of Privacy Policy: A website must have a clear and accessible privacy policy. Not having one can damage trust and may also violate laws or regulations.

```html
<!DOCTYPE html>
<html lang="en">
<head>
<meta charset="utf-8">
<title>Stridewell Equine Insurance</title>
<link href="https://fonts.googleapis.com/css2?family=Oswald:wght@500;600;700&family=Montserrat:wght@400;500;600&display=swap" rel="stylesheet">
<style>
:root{
  --yellow:#fdb913;
  --yellow-deep:#f2a900;
  --ink:#111111;
  --charcoal:#333333;
  --text:#3a3a3a;
  --cream:#fcf7ec;
  --grey:#f2f2f2;
  --white:#ffffff;
  --night:#0a0a0a;
}
*{box-sizing:border-box;margin:0;padding:0}
html,body{width:1200px;height:4246px;overflow:hidden}
body{font-family:"Montserrat",sans-serif;color:var(--text);background:var(--white);position:relative}
.head-font{font-family:"Oswald",sans-serif}
.accent{color:var(--yellow)}
.abs{position:absolute}

/* nav */
.nav{position:absolute;left:63px;top:33px;width:1058px;height:79px;background:var(--white);border-radius:40px;z-index:5;display:flex;align-items:center;padding:0 30px 0 38px;box-shadow:0 2px 10px rgba(0,0,0,.08)}
.brand{display:flex;align-items:center;gap:10px;font-family:"Oswald",sans-serif;font-weight:600;font-size:34px;letter-spacing:3px;color:var(--ink)}
.brand-dot{width:34px;height:34px;border-radius:50%;border:3px solid var(--ink)}
.nav-links{display:flex;gap:33px;margin-left:auto;font-size:15px;color:var(--ink);font-weight:500}
.nav-signin{margin-left:34px;background:var(--yellow);color:var(--ink);font-family:"Oswald",sans-serif;font-weight:600;font-size:15px;padding:6px 18px;border-radius:18px}

/* hero */
.hero{position:absolute;left:0;top:0;width:1200px;height:725px;background:var(--cream)}
.hero-photo{position:absolute;left:0;top:0;width:1200px;height:660px;background:linear-gradient(180deg,#9ec4e6 0%,#c7dcef 40%,#b9c7a4 70%,#8f9c62 100%)}
.hero-wave{position:absolute;left:0;top:500px}
.hero-copy{position:absolute;right:156px;top:180px;text-align:right;width:420px}
.hero-title{font-family:"Oswald",sans-serif;font-weight:700;font-size:54px;line-height:62px;color:var(--white);letter-spacing:1px;text-shadow:0 2px 4px rgba(0,0,0,.25)}
.hero-sub{font-weight:600;font-size:22px;color:var(--white);margin-top:8px}
.hero-text{font-size:15px;line-height:25px;color:var(--white);margin-top:14px}
.hero-btns{display:flex;justify-content:flex-end;gap:10px;margin-top:14px}
.btn{display:inline-block;font-family:"Oswald",sans-serif;font-weight:600;font-size:15px;color:var(--ink);background:var(--yellow);padding:6px 14px;border-radius:18px;letter-spacing:.3px}
.btn-ghost{background:transparent;border:2px solid var(--white);color:var(--white);padding:4px 16px}
.dots{position:absolute;left:1139px;top:258px;display:flex;flex-direction:column;gap:16px}
.dots span{width:12px;height:12px;border-radius:50%;border:2px solid var(--white)}
.dots .on{background:var(--yellow);border-color:var(--yellow)}

/* about */
.about{position:absolute;left:0;top:725px;width:1200px;height:552px;background:var(--cream)}
.section-title{font-family:"Oswald",sans-serif;font-weight:700;font-size:40px;color:var(--ink);letter-spacing:.5px}
.about-copy{position:absolute;left:104px;top:68px;width:500px}
.about-sub{font-weight:600;font-size:21px;color:var(--ink);margin-top:16px}
.about-copy p{font-size:14px;line-height:23.5px;margin-top:10px}
.about-copy .btn{margin-top:16px;font-size:14px}
.about-media{position:absolute;left:643px;top:15px;width:428px;height:428px;border-radius:50%;background:radial-gradient(circle at 50% 45%,#e8a35a 0%,#3a7ea0 35%,#123049 70%,#0b1a2a 100%)}
.play{position:absolute;left:194px;top:194px;width:40px;height:40px;border-radius:50%;background:var(--yellow);display:flex;align-items:center;justify-content:center}
.about-swoosh{position:absolute;left:850px;top:10px}

/* services */
.services{position:absolute;left:0;top:1277px;width:1200px;height:577px;background:var(--white)}
.centered-title{position:absolute;left:0;width:1200px;text-align:center}
.title-rule{position:absolute;left:553px;width:94px;height:3px;background:var(--yellow)}
.svc{position:absolute;top:218px;width:233px;height:277px;background:var(--charcoal);border-radius:4px;text-align:center;padding:58px 16px 0}
.svc.active{background:var(--yellow)}
.svc-icon{position:absolute;left:76px;top:-42px}
.svc h3{font-family:"Oswald",sans-serif;font-weight:600;font-size:19px;color:var(--yellow)}
.svc.active h3{color:var(--ink)}
.svc p{font-size:12.5px;line-height:21px;color:#e6e6e6;margin-top:10px}
.svc.active p{color:#6a4d00}
.svc .btn{margin-top:12px;font-size:14px;padding:5px 16px}
.svc.active .btn{background:transparent;border:2px solid var(--ink);padding:3px 18px}

/* products */
.products{position:absolute;left:0;top:1854px;width:1200px;height:570px;background:var(--grey)}
.product{position:absolute;top:208px;width:316px;height:316px;border-radius:3px}
.product-label{position:absolute;left:15px;top:278px;width:285px;height:69px;background:var(--yellow);border-radius:3px;font-family:"Oswald",sans-serif;font-weight:600;font-size:28px;color:var(--ink);display:flex;align-items:center;justify-content:center;box-shadow:0 3px 8px rgba(0,0,0,.15)}

/* faqs */
.faqs{position:absolute;left:0;top:2424px;width:1200px;height:625px;background:var(--white)}
.faq-box{position:absolute;left:104px;top:150px;width:992px;height:396px;background:var(--white);box-shadow:0 2px 14px rgba(0,0,0,.1)}
.faq-media{position:absolute;left:0;top:0;width:498px;height:396px;background:radial-gradient(circle at 50% 35%,#d9e4f2 0%,#3f6a92 30%,#1b3450 65%,#0e1d30 100%)}
.faq-list{position:absolute;left:522px;top:32px;width:444px}
.faq-item{height:52px;border:1px solid #555;border-bottom:none;display:flex;align-items:center;justify-content:space-between;padding:0 14px 0 16px;font-family:"Oswald",sans-serif;font-weight:500;font-size:17px;color:var(--charcoal)}
.faq-open{border:1px solid #f0e3c0;box-shadow:0 2px 8px rgba(0,0,0,.08);padding:10px 16px 14px}
.faq-open .faq-q{display:flex;justify-content:space-between;font-family:"Oswald",sans-serif;font-weight:500;font-size:18px;color:var(--yellow)}
.faq-open p{font-size:9.5px;line-height:16px;color:#555;margin-top:8px}

/* blog */
.blog{position:absolute;left:0;top:3049px;width:1200px;height:760px;background:var(--cream)}
.post{position:absolute;top:198px;width:303px;height:351px}
.post-caption{position:absolute;left:0;bottom:26px;width:100%;text-align:center;font-family:"Oswald",sans-serif;font-weight:600;font-size:19px;line-height:26px;color:var(--white)}
.post.featured{background:#cfa21c;text-align:center;padding:40px 30px 0}
.post.featured h3{font-family:"Oswald",sans-serif;font-weight:600;font-size:19px;line-height:27px;color:var(--ink)}
.post.featured p{font-size:14px;line-height:23px;color:#2b2200;margin-top:12px}
.post.featured .more{font-family:"Oswald",sans-serif;font-weight:600;font-size:19px;color:var(--ink);margin-top:16px}
.blog-cta{position:absolute;left:541px;top:605px;font-size:14px}

/* footer */
.footer{position:absolute;left:0;top:3760px;width:1200px;height:486px}
.footer-bg{position:absolute;left:0;top:0}
.footer-brand{position:absolute;left:104px;top:144px;display:flex;align-items:center;gap:14px;font-family:"Oswald",sans-serif;font-weight:600;font-size:50px;letter-spacing:3px;color:var(--white)}
.footer-brand .brand-dot{width:50px;height:50px;border-color:var(--white)}
.footer-about{position:absolute;left:104px;top:246px;width:330px;font-size:14px;line-height:22px;color:#e8e8e8}
.socials{position:absolute;left:104px;top:343px;display:flex;gap:16px}
.socials span{width:30px;height:30px;border-radius:50%;border:2px solid var(--yellow)}
.footer-h{font-family:"Montserrat",sans-serif;font-weight:600;font-size:25px;color:var(--white)}
.quick{position:absolute;left:473px;top:150px}
.quick-cols{display:flex;gap:62px;margin-top:18px}
.quick-cols ul{list-style:none;font-size:13px;line-height:25px;color:#e8e8e8}
.touch{position:absolute;left:771px;top:150px;width:272px}
.field{background:var(--white);height:30px;font-size:11px;color:#555;padding:8px 10px;margin-top:10px}
.field-row{display:flex;gap:10px}
.field-row .field{flex:1}
.touch .field-row{margin-top:20px}
.touch .field-row .field{margin-top:0}
.field.msg{height:66px}
.submit{position:absolute;left:196px;top:286px;font-size:13px;padding:4px 18px}
.chat{position:absolute;left:1118px;top:120px;width:58px;height:58px;border-radius:50%;border:3px solid var(--yellow);display:flex;align-items:center;justify-content:center}
.copyright{position:absolute;left:0;top:437px;width:1200px;text-align:center;font-size:12px;color:#e8e8e8}
</style>
</head>
<body>

<header class="nav">
  <div class="brand"><span class="brand-dot"></span>STRIDEWELL</div>
  <nav class="nav-links">
    <span>Home</span><span>Services</span><span>Product</span><span>File a Claim</span><span>FAQS</span><span>Blog</span><span>Contact Us</span>
  </nav>
  <span class="nav-signin">SIGN IN</span>
</header>

<section class="hero">
  <div class="hero-photo" role="img" aria-label="Rider in a white shirt on a chestnut horse cantering across an open field under a bright sky"></div>
  <svg class="hero-wave" width="1200" height="225" viewBox="0 0 1200 225" aria-hidden="true">
    <path d="M0 110 C180 150 300 150 430 120 C600 80 760 20 920 28 C1040 34 1130 60 1200 90 L1200 225 L0 225 Z" fill="#fcf7ec"/>
    <path d="M0 108 C180 150 300 150 430 120 C600 78 760 16 920 22 C1040 28 1130 56 1200 86 L1200 70 C1120 34 1030 8 920 4 C760 -2 600 60 430 100 C300 130 180 140 0 108 Z" fill="#fdb913"/>
  </svg>
  <div class="hero-copy">
    <h1 class="hero-title">WELCOME TO<br>STRIDEWELL</h1>
    <div class="hero-sub">Equine Insurance</div>
    <p class="hero-text">Lorem ipsum dolor sit amet, consectetur do eiusmod tempor incididunt ut labore et dolore magna aliqua.</p>
    <div class="hero-btns"><span class="btn btn-ghost">QUOTE CALCULATOR</span><span class="btn">GET A QUOTE</span></div>
  </div>
  <div class="dots"><span></span><span class="on"></span><span></span></div>
</section>

<section class="about">
  <div class="about-copy">
    <h2 class="section-title">ABOUT TO <span class="accent">STRIDEWELL</span></h2>
    <div class="about-sub">Equine Insurance</div>
    <p>Lorem ipsum dolor sit amet, consectetur adipiscing elit, sed do eiusmod tempor incididunt ut labore et dolore magna aliqua. Ut enim ad minim veniam, quis nostrud exercitation ullamco laboris nisi ut aliquip ex ea commodo consequat.</p>
    <p>Sed ut perspiciatis unde omnis iste natus error sit voluptatem accusantium doloremque laudantium, totam rem aperiam, eaque ipsa quae ab illo inventore veritatis et quasi architecto beatae vitae dicta sunt explicabo. Nemo enim ipsam voluptatem quia voluptas sit aspernatur.</p>
    <span class="btn">CALL US TODAY!</span>
  </div>
  <svg class="about-swoosh" width="300" height="420" viewBox="0 0 300 420" aria-hidden="true">
    <path d="M40 10 C180 40 240 200 200 300 C170 370 110 400 60 410 C140 380 200 320 210 240 C220 150 160 60 40 10 Z" fill="#fdb913"/>
    <path d="M120 380 C190 350 250 300 295 270" stroke="#fdb913" stroke-width="5" fill="none"/>
    <path d="M110 392 C200 370 260 330 295 300" stroke="#fdb913" stroke-width="3" fill="none"/>
  </svg>
  <div class="about-media" role="img" aria-label="Video still of two glowing digital hands meeting in a handshake over a network backdrop">
    <span class="play"><svg width="16" height="16" viewBox="0 0 16 16"><path d="M4 2 L14 8 L4 14 Z" fill="#fff"/></svg></span>
  </div>
</section>

<section class="services">
  <h2 class="section-title centered-title" style="top:66px">STRIDEWELL <span class="accent">SERVICES</span></h2>
  <span class="title-rule" style="top:130px"></span>

  <article class="svc" style="left:79px">
    <svg class="svc-icon" width="82" height="90" viewBox="0 0 82 90"><path d="M41 0 L82 22 L82 68 L41 90 L0 68 L0 22 Z" fill="#fdb913"/><rect x="26" y="30" width="30" height="28" rx="3" fill="#222"/><rect x="26" y="30" width="30" height="7" fill="#222"/><path d="M32 47 l5 5 l10 -10" stroke="#fdb913" stroke-width="3" fill="none"/><rect x="31" y="26" width="3" height="7" fill="#222"/><rect x="48" y="26" width="3" height="7" fill="#222"/></svg>
    <h3>Lorem Ipsum Dolor</h3>
    <p>Lorem ipsum dolor sit amet, consectetur adipiscing elit, sed do eiusmod tempor incididunt ut labore et dolore magna aliqua.</p>
    <span class="btn">READ MORE</span>
  </article>
  <article class="svc" style="left:349px">
    <svg class="svc-icon" width="82" height="90" viewBox="0 0 82 90"><path d="M41 0 L82 22 L82 68 L41 90 L0 68 L0 22 Z" fill="#fdb913"/><circle cx="41" cy="42" r="6" fill="#222"/><path d="M30 62 a11 10 0 0 1 22 0 Z" fill="#222"/><circle cx="27" cy="40" r="4" fill="#222"/><circle cx="55" cy="40" r="4" fill="#222"/><path d="M19 56 a8 7 0 0 1 14 0 Z M49 56 a8 7 0 0 1 14 0 Z" fill="#222"/><rect x="31" y="22" width="20" height="10" rx="2" fill="#222"/></svg>
    <h3>Lorem Ipsum Dolor</h3>
    <p>Lorem ipsum dolor sit amet, consectetur adipiscing elit, sed do eiusmod tempor incididunt ut labore et dolore magna aliqua.</p>
    <span class="btn">READ MORE</span>
  </article>
  <article class="svc active" style="left:618px">
    <svg class="svc-icon" width="82" height="90" viewBox="0 0 82 90"><path d="M41 0 L82 22 L82 68 L41 90 L0 68 L0 22 Z" fill="#333"/><circle cx="46" cy="34" r="10" fill="#fdb913"/><text x="46" y="39" text-anchor="middle" font-family="Montserrat,sans-serif" font-size="13" font-weight="600" fill="#333">$</text><path d="M18 54 h10 l10 4 h12 l12 -6 v6 l-14 8 h-20 h-10 Z" fill="#fdb913"/></svg>
    <h3>Lorem Ipsum Dolor</h3>
    <p>Lorem ipsum dolor sit amet, consectetur adipiscing elit, sed do eiusmod tempor incididunt ut labore et dolore magna aliqua.</p>
    <span class="btn">READ MORE</span>
  </article>
  <article class="svc" style="left:887px">
    <svg class="svc-icon" width="82" height="90" viewBox="0 0 82 90"><path d="M41 0 L82 22 L82 68 L41 90 L0 68 L0 22 Z" fill="#fdb913"/><rect x="26" y="24" width="24" height="34" rx="2" fill="#222"/><rect x="30" y="31" width="14" height="3" fill="#fdb913"/><rect x="30" y="38" width="14" height="3" fill="#fdb913"/><circle cx="52" cy="56" r="9" fill="#222" stroke="#fdb913" stroke-width="2"/><path d="M47 56 l4 4 l6 -7" stroke="#fdb913" stroke-width="2.5" fill="none"/></svg>
    <h3>Lorem Ipsum Dolor</h3>
    <p>Lorem ipsum dolor sit amet, consectetur adipiscing elit, sed do eiusmod tempor incididunt ut labore et dolore magna aliqua.</p>
    <span class="btn">READ MORE</span>
  </article>
</section>

<section class="products">
  <h2 class="section-title centered-title" style="top:112px">STRIDEWELL <span class="accent">PRODUCT</span></h2>
  <span class="title-rule" style="top:176px"></span>
  <div class="product" style="left:92px;background:linear-gradient(180deg,#10223f 0%,#2a5c8c 55%,#b44fa8 100%)" role="img" aria-label="Glowing circuit cloud illustration in blue and pink"><div class="product-label">Lorem ipsum</div></div>
  <div class="product" style="left:442px;background:linear-gradient(160deg,#1d3b5e 0%,#0f2036 60%,#2b6c7c 100%)" role="img" aria-label="Computer chip labelled with AI and chat bubbles"><div class="product-label">Lorem ipsum</div></div>
  <div class="product" style="left:793px;background:linear-gradient(180deg,#bfc2c6 0%,#7b7f85 50%,#3c3f44 100%)" role="img" aria-label="Hands typing on a laptop with a search bar and chat bubbles overlay"><div class="product-label">Lorem ipsum</div></div>
</section>

<section class="faqs">
  <h2 class="section-title centered-title" style="top:56px">INTERACTIVE <span class="accent">FAQS</span></h2>
  <span class="title-rule" style="top:120px"></span>
  <div class="faq-box">
    <div class="faq-media" role="img" aria-label="Robotic hand and human hand reaching toward a glowing light bulb"></div>
    <div class="faq-list">
      <div class="faq-item">Lorem ipsum dolor sit amet ?<svg width="12" height="12" viewBox="0 0 12 12"><circle cx="6" cy="6" r="6" fill="#333"/><path d="M3 5 l3 3 l3 -3" stroke="#fff" stroke-width="1.5" fill="none"/></svg></div>
      <div class="faq-item">Amet consectetur adipiscing ?<svg width="12" height="12" viewBox="0 0 12 12"><circle cx="6" cy="6" r="6" fill="#333"/><path d="M3 5 l3 3 l3 -3" stroke="#fff" stroke-width="1.5" fill="none"/></svg></div>
      <div class="faq-item">Sed ut perspiciatis unde omnis<svg width="12" height="12" viewBox="0 0 12 12"><circle cx="6" cy="6" r="6" fill="#333"/><path d="M3 5 l3 3 l3 -3" stroke="#fff" stroke-width="1.5" fill="none"/></svg></div>
      <div class="faq-open">
        <div class="faq-q">Voluptatem accusantium ?<svg width="12" height="12" viewBox="0 0 12 12"><circle cx="6" cy="6" r="6" fill="#fdb913"/><path d="M3 7 l3 -3 l3 3" stroke="#fff" stroke-width="1.5" fill="none"/></svg></div>
        <p>Lorem ipsum dolor sit amet, consectetur adipiscing elit, sed do eiusmod tempor incididunt ut labore et dolore magna aliqua. Ut enim ad minim veniam, quis nostrud exercitation ullamco laboris nisi ut aliquip ex ea commodo consequat. Duis aute irure dolor in reprehenderit in voluptate velit esse cillum dolore eu fugiat nulla pariatur. Excepteur sint occaecat cupidatat non proident, sunt in culpa qui officia deserunt mollit anim id est laborum.</p>
      </div>
    </div>
  </div>
</section>

<section class="blog">
  <h2 class="section-title centered-title" style="top:88px">FEATURE <span class="accent">BLOG</span></h2>
  <span class="title-rule" style="top:152px"></span>
  <article class="post" style="left:104px;background:linear-gradient(180deg,#f1eeee 0%,#cfc7c4 55%,#5a5250 100%)" role="img" aria-label="Hands signing a document with a pen">
    <div class="post-caption">Lorem ipsum dolor sit amet,<br>consectetur</div>
  </article>
  <article class="post featured" style="left:448px">
    <h3>Lorem ipsum dolor sit amet,<br>consectetur</h3>
    <p>Lorem ipsum dolor sit amet, consectetur adipiscing elit, sed do eiusmod tempor incididunt ut labore et dolore magna aliqua.</p>
    <div class="more">Read More »</div>
  </article>
  <article class="post" style="left:793px;background:linear-gradient(135deg,#1f4f9a 0%,#15306a 50%,#b8324a 100%)" role="img" aria-label="Robot figure touching a holographic interface">
    <div class="post-caption">Lorem ipsum dolor sit amet,<br>consectetur</div>
  </article>
  <span class="btn blog-cta">CALL US TODAY!</span>
</section>

<footer class="footer">
  <svg class="footer-bg" width="1200" height="486" viewBox="0 0 1200 486" aria-hidden="true">
    <path d="M0 20 C220 60 420 100 620 96 C850 92 1040 40 1200 0 L1200 486 L0 486 Z" fill="#0a0a0a"/>
    <path d="M0 14 C220 56 420 92 620 88 C850 84 1040 30 1200 -6 L1200 10 C1040 50 850 108 620 112 C420 114 220 74 0 30 Z" fill="#fdb913"/>
  </svg>
  <div class="footer-brand"><span class="brand-dot"></span>STRIDEWELL</div>
  <p class="footer-about">Lorem ipsum dolor sit amet, consectetur adipiscing elit, sed do eiusmod tempor incididunt ut labore et dolore magna aliqua</p>
  <div class="socials" aria-label="Social links"><span></span><span></span><span></span></div>

  <div class="quick">
    <div class="footer-h">Quick Links</div>
    <div class="quick-cols">
      <ul><li>Home</li><li>Services</li><li>Product</li><li>File a Claim</li><li>FAQS</li><li>Blog</li><li>Contact Us</li></ul>
      <ul><li>Terms &amp; conditions</li><li>Privacy Policy</li><li>About Us</li><li>Support</li></ul>
    </div>
  </div>

  <div class="touch">
    <div class="footer-h">Get In Touch</div>
    <div class="field-row"><div class="field">Name :</div><div class="field">Phone :</div></div>
    <div class="field">Email :</div>
    <div class="field msg">Message :</div>
    <span class="btn submit">SUBMIT</span>
  </div>

  <div class="chat"><svg width="28" height="28" viewBox="0 0 28 28"><rect x="3" y="4" width="22" height="16" rx="3" fill="#fdb913"/><path d="M8 20 l0 6 l6 -6 Z" fill="#fdb913"/><rect x="8" y="9" width="12" height="2" fill="#0a0a0a"/><rect x="8" y="13" width="8" height="2" fill="#0a0a0a"/></svg></div>
  <p class="copyright">Copyrights © 2022 Stridewell | Rights Reserved</p>
</footer>

</body>
</html>
```